Tea standup pouch labels

Dear designers,
I need a minimalistic and modern label for my loose tea stand-up pouches (100, 250 and 500gm packs). The label should cover 70-80% of the pouch face (front and rear both).
The label will be 2 part label - Front and Rear side labels.
The labels should have a green background (Pantone Green C) with Golden or White or black colour text. Please either use the Golden logo or black logo to see which looks good with Pantone Green C background.
I am also attaching the content file and a few other files (Assam tea logo) to be used in the label.
The Assam tea logo should be small at the bottom left or right side of the front side. The logo should be dominant on the front page (some of the designs I received have small logo and big "100% single estate tea" and "Assam logo" as big characters on the front page which is not what I am looking for.

The font style should note simple Times new roman or Arial. It should look modern and should be something matching to the logo sentence 'Freshest possible' but should also not be in italics. Please refer to files Font style reference front and back for the style of font. Also use the same box space design on the rear - Content should be in White background; the rectangular box edges should be rounded and the border should be in dual colour - Golden and white or in black and white depending on the logo colour used (golden or black).

For the Rear page - headings could be in Golden colour or black colour depending on the logo colour you choose to use and the text can be in white colour i.e. Option 1 - Headings in golden colour and text in white colour; Option 2 - Heading in Black colour and text in white colour or any other combination that looks good - designer to decide.

Please let me know if you need any further information.

thanks,
Toral

```html
<!DOCTYPE html>
<html lang="en">
<head>
<meta charset="utf-8">
<title>Brewleaf – Front Pouch Label</title>
<link rel="stylesheet" href="https://fonts.googleapis.com/css2?family=Roboto+Condensed:wght@100;300;400;700&family=Mrs+Saint+Delafield&display=swap">
<style>
  :root {
    --teal: #35b7a5;
    --mint-band: #c0f8f1;
    --leaf-mint: #c6f6f0;
    --leaf-pale: #eafcf9;
    --paper: #ffffff;
    --ink: #0d1a1a;
    --white: #ffffff;
  }
  * { box-sizing: border-box; margin: 0; padding: 0; }
  html, body {
    width: 860px;
    height: 1200px;
    overflow: hidden;
    background: var(--paper);
  }
  .label {
    position: relative;
    width: 860px;
    height: 1200px;
    background: var(--paper);
    font-family: "Roboto Condensed", "Arial Narrow", sans-serif;
    color: var(--ink);
  }
  .brand-panel {
    position: absolute;
    left: 0; top: 0;
    width: 860px; height: 740px;
    background: var(--teal);
  }
  .brand-name {
    position: absolute;
    left: 0; right: 0;
    text-align: center;
    font-family: "Roboto Condensed", "Arial Narrow", sans-serif;
    font-weight: 100;
    font-size: 140px;
    line-height: 1;
    letter-spacing: 0.16em;
    padding-left: 0.16em;
    color: var(--white);
  }
  .brand-name--top { top: 82px; }
  .brand-name--bottom { top: 455px; }
  .brand-mark {
    position: absolute;
    left: 366px;
    top: 268px;
    width: 128px;
    height: 128px;
  }
  .tagline {
    position: absolute;
    left: 0; right: 0;
    top: 612px;
    text-align: center;
    font-family: "Mrs Saint Delafield", cursive;
    font-weight: 400;
    font-size: 62px;
    line-height: 1;
    color: var(--white);
  }
  .claim-band {
    position: absolute;
    left: 0; top: 741px;
    width: 860px; height: 76px;
    background: var(--mint-band);
    display: flex;
    align-items: center;
    justify-content: center;
  }
  .claim-text {
    font-weight: 400;
    font-size: 42px;
    letter-spacing: 0.2em;
    padding-left: 0.2em;
    color: var(--ink);
  }
  .leaf-pattern {
    position: absolute;
    left: 0; top: 817px;
    width: 860px; height: 370px;
    background:
      radial-gradient(ellipse at 20% 30%, var(--leaf-mint) 0%, transparent 55%),
      radial-gradient(ellipse at 80% 70%, var(--leaf-mint) 0%, transparent 55%),
      linear-gradient(180deg, var(--leaf-pale), #d8faf5);
  }
  .net-weight {
    position: absolute;
    left: 0; right: 0;
    top: 1100px;
    text-align: center;
    line-height: 1.3;
  }
  .net-weight__label {
    font-weight: 400;
    font-size: 31px;
    letter-spacing: 0.1em;
  }
  .net-weight__value {
    font-weight: 700;
    font-size: 32px;
    letter-spacing: 0.08em;
  }
  .origin-badge {
    position: absolute;
    left: 690px;
    top: 1062px;
    width: 114px;
    height: 114px;
  }
  .base-stripe {
    position: absolute;
    left: 0; bottom: 0;
    width: 860px; height: 13px;
    background: var(--teal);
  }
</style>
</head>
<body>
  <main class="label">
    <section class="brand-panel">
      <h1 class="brand-name brand-name--top">BREW</h1>
      <svg class="brand-mark" viewBox="0 0 128 128" aria-hidden="true">
        <circle cx="64" cy="64" r="60" fill="none" stroke="#ffffff" stroke-width="4"/>
      </svg>
      <p class="brand-name brand-name--bottom" aria-hidden="true">LEAF</p>
      <p class="tagline">freshest possible</p>
    </section>

    <section class="claim-band">
      <p class="claim-text">100% Single Estate Tea</p>
    </section>

    <div class="leaf-pattern" role="img" aria-label="Repeating pattern of small pale mint tea leaves on white"></div>

    <div class="net-weight">
      <p class="net-weight__label">Net Wt.</p>
      <p class="net-weight__value">250g/8.82oz</p>
    </div>

    <svg class="origin-badge" viewBox="0 0 114 114" role="img" aria-label="Regional origin certification badge">
      <circle cx="57" cy="57" r="54" fill="#ffffff" stroke="#0d1a1a" stroke-width="3"/>
    </svg>

    <div class="base-stripe"></div>
  </main>
</body>
</html>
```